Business Card Design Project

We are a consulting company which works with tourism operators and attractions, wineries, heritage sites, National and conservation parks etc to help them identify their 'Point of Difference' and then deliver an exceptional tourism visitor experience.
We specialise in: Operator training, Site interpretation, Product and experience development, Planning and analysis.
We have a tag line of "Telling your story - really well."
The company name is MornVoice and the logo is this word with the 'Morn' in black and the 'Voice' in orange - but this can be changed. The 'a' is a speech bubble. A lot of what we do involves talking!
The design should communicate that we can make a big difference to the range and quality of experiences that visitors get at your site.
Updates

I put the wrong telephone number in my brief. My apologies.

It should be +61 0487 555 913

Target Market(s)

tourism busineses, wineries and cellar doors, heritage sites, environment managers, Government agencies & private companies

Industry/Entity Type

Tourism

Requirements
Must have
• Name: Ruth Pellow
Title: Emeritus Professor
Qualifications: BSc(Hons), PhD
Role: Director
Address: PO Box 317, Harlow Bay, South Australia 5071
Phone: (+61) 0487 555 913
Email: ruth@mornvoice-example.com.au
www.mornvoice-example.com.au
ABN 514 072 389 16

Operator Training, Site Interpretation, Product and Experience Development, Planning and Analysis.
Nice to have
• Awards:
Winner 2011 Coastline Visitor Honours – Kestrel College - Tourism Education and Training
Winner 2009 Coastline Visitor Honours - Outstanding Contribution by an Individual
Winner 2009 Gulfside Citizen Medal - Tourism Award
Should not have
• No 'shadows' to company name/logo please.
No black reverse side of card

```html
<!DOCTYPE html>
<html lang="en">
<head>
<meta charset="utf-8">
<title>MornVoice Business Card</title>
<link rel="stylesheet" href="https://fonts.googleapis.com/css2?family=Open+Sans:wght@400;600;700&family=Arimo:wght@400&display=swap">
<style>
  :root {
    --bg: #dcdcde;
    --card: #ffffff;
    --ink: #1c1c1c;
    --orange: #e0700f;
    --band-black: #0d0d0d;
    --muted: #8a8a8a;
  }
  * { margin: 0; padding: 0; box-sizing: border-box; }
  html, body { width: 1200px; height: 1037px; overflow: hidden; background: var(--bg); }
  .stage { position: relative; width: 1200px; height: 1037px; }

  .card {
    position: absolute;
    left: 220px;
    width: 760px;
    height: 434px;
    background: var(--card);
    font-family: "Open Sans", Arial, sans-serif;
    color: var(--ink);
    overflow: hidden;
  }
  .card--back { top: 52px; }
  .card--front { top: 551px; }

  .logo { position: absolute; display: flex; align-items: center; gap: 10px; }
  .logo__mark { width: 14px; height: 14px; background: var(--orange); }
  .logo__name { font-weight: 700; color: var(--ink); letter-spacing: -1px; line-height: 1; }
  .logo__tagline { position: absolute; color: var(--muted); letter-spacing: 1px; }

  .card--back .logo { left: 205px; top: 168px; }
  .card--back .logo__name { font-size: 62px; }
  .card--back .logo__tagline { left: 330px; top: 238px; font-size: 12px; }

  .card--front .logo { left: 48px; top: 48px; }
  .card--front .logo__name { font-size: 46px; }
  .card--front .logo__tagline { left: 150px; top: 104px; font-size: 11px; }

  .band { position: absolute; height: 14px; }
  .band--black { background: var(--band-black); left: 0; }
  .band--orange { background: var(--orange); right: 0; }
  .card--back .band { top: 352px; }
  .card--back .band--black { width: 398px; }
  .card--back .band--orange { left: 398px; }
  .card--front .band { top: 364px; }
  .card--front .band--black { width: 380px; }
  .card--front .band--orange { left: 380px; }

  .band-mark {
    position: absolute; font-size: 14px; font-weight: 700; color: var(--ink);
    letter-spacing: -0.5px;
  }
  .card--back .band-mark { right: 30px; top: 332px; }
  .card--front .band-mark { right: 30px; top: 392px; }

  .contact {
    position: absolute; left: 48px; top: 250px;
    font-family: "Arimo", Arial, sans-serif; font-size: 19px; line-height: 26px; color: var(--ink);
    list-style: none;
  }
  .contact li { display: flex; align-items: center; gap: 12px; }
  .contact__icon { width: 16px; height: 16px; flex: none; }
  .contact__plain { padding-left: 28px; }

  .person { position: absolute; right: 60px; top: 112px; text-align: center; width: 280px; }
  .person__name { font-size: 22px; font-weight: 400; }
  .person__title { font-size: 18px; color: var(--orange); margin-top: 2px; }
  .person__quals { font-size: 16px; margin-top: 30px; line-height: 24px; }
  .address {
    position: absolute; right: 60px; top: 278px; width: 280px; text-align: center;
    font-size: 19px; line-height: 25px; color: var(--orange);
  }
</style>
</head>
<body>
<main class="stage">

  <section class="card card--back" aria-label="Card reverse">
    <div class="logo">
      <span class="logo__mark"></span>
      <span class="logo__name">MornVoice</span>
    </div>
    <span class="logo__tagline">tell well</span>
    <div class="band band--black"></div>
    <div class="band band--orange"></div>
    <span class="band-mark">MornVoice</span>
  </section>

  <section class="card card--front" aria-label="Card front">
    <div class="logo">
      <span class="logo__mark"></span>
      <span class="logo__name">MornVoice</span>
    </div>
    <span class="logo__tagline">tell well</span>

    <ul class="contact">
      <li>
        <svg class="contact__icon" viewBox="0 0 16 16" aria-hidden="true">
          <circle cx="8" cy="8" r="8" fill="var(--orange)"/>
          <path d="M5 4.5c0 3.5 3 6.5 6.5 6.5l.8-1.6-1.8-.9-.8.8c-1-.5-2-1.5-2.5-2.5l.8-.8-.9-1.8z" fill="#fff"/>
        </svg>
        <span>(+61) 0487 555 913</span>
      </li>
      <li>
        <svg class="contact__icon" viewBox="0 0 16 16" aria-hidden="true">
          <circle cx="8" cy="8" r="8" fill="var(--orange)"/>
          <rect x="3.5" y="5" width="9" height="6" fill="#fff"/>
          <path d="M3.5 5 8 8.5 12.5 5" fill="none" stroke="var(--orange)" stroke-width="1"/>
        </svg>
        <span>ruth@mornvoice-example.com.au</span>
      </li>
      <li>
        <svg class="contact__icon" viewBox="0 0 16 16" aria-hidden="true">
          <circle cx="8" cy="8" r="8" fill="var(--orange)"/>
          <circle cx="8" cy="8" r="4.5" fill="none" stroke="#fff" stroke-width="1.2"/>
          <path d="M3.5 8h9M8 3.5c-2 2.5-2 6.5 0 9M8 3.5c2 2.5 2 6.5 0 9" fill="none" stroke="#fff" stroke-width="1"/>
        </svg>
        <span>www.mornvoice-example.com.au</span>
      </li>
      <li class="contact__plain">ABN 514 072 389 16</li>
    </ul>

    <div class="band band--black"></div>
    <div class="band band--orange"></div>

    <div class="person">
      <p class="person__name">Ruth Pellow</p>
      <p class="person__title">Emeritus Professor</p>
      <p class="person__quals">BSc(Hons), PhD<br>Director</p>
    </div>
    <p class="address">PO Box 317, Harlow Bay,<br>South Australia 5071</p>

    <span class="band-mark">MornVoice</span>
  </section>

</main>
</body>
</html>
```